One page Flyer for Magician

I'm after a one Page Flyer

A4 Size - One sided
I want the finished artwork in 2 Forms.
One with the URL and one without the URL.

I need to be able to either print out myself in a small run ( I have a Brivo Chroma Tonerline)
or send out as a PDF attachment
or use on Website

I have attached the copy that should be included. 2 Words New doc
The Order of the sentences / testimonials / client list / locations worked
is not set so can be changed or played with to create a strong final image

I have attached one image to be incorporated

As you can see from the copy (or a visit to my website)
I'm after something that is -

Classy , Sophisticated, Smart, perhaps a bit quirky.

You can add other design elements in if needed , but Nothing "Corny Magic" like - eg no Rabbits , Wands, puffs of smoke

I have no corporate colour or logo or branding that should be included so you have a fairly free reign

```html
<!DOCTYPE html>
<html lang="en">
<head>
<meta charset="utf-8">
<title>Julian Marsh – Mentalist Flyer</title>
<link rel="stylesheet" href="https://fonts.googleapis.com/css2?family=Cinzel:wght@400;500&family=Titan+One&family=Baloo+2:wght@500&family=Arimo:ital,wght@0,400;0,700;1,400;1,700&family=Archivo+Black&family=Noto+Serif:ital,wght@1,700&display=swap">
<style>
  :root {
    --sky: #8fbde6;
    --sky-pale: #c3d9f1;
    --ink-blue: #3d4a9c;
    --night: #0b0d14;
    --night-mid: #1a1e2c;
    --panel: rgba(140, 165, 205, 0.5);
    --white: #ffffff;
    --text: #111111;
    --star: #b9bde6;
  }
  * { box-sizing: border-box; margin: 0; padding: 0; }
  html, body { width: 927px; height: 1200px; overflow: hidden; background: var(--white); }
  .flyer { position: relative; width: 927px; height: 1200px; overflow: hidden; font-family: "Arimo", Arial, sans-serif; color: var(--text); }

  .starfield {
    position: absolute; left: 0; top: 120px; width: 927px; height: 780px;
    background: radial-gradient(ellipse at 70% 60%, var(--night-mid), var(--night) 70%);
  }
  .sky-curve { position: absolute; left: 0; top: 0; width: 927px; height: 420px; }

  .headline {
    position: absolute; top: 28px; left: 0; width: 927px; text-align: center;
    font-family: "Cinzel", serif; font-weight: 500; color: var(--ink-blue);
    font-size: 38px; line-height: 44px; letter-spacing: 1px;
  }
  .performer-name {
    position: absolute; top: 118px; left: 0; width: 927px; text-align: center;
    font-family: "Titan One", sans-serif; font-size: 96px; color: var(--white);
    letter-spacing: 2px; transform: rotate(-1deg);
    text-shadow: 4px 6px 6px rgba(0,0,0,0.75);
  }

  .portrait {
    position: absolute; border: 9px solid var(--white);
    box-shadow: 3px 4px 8px rgba(0,0,0,0.6);
    background: linear-gradient(160deg, #9a9a9a, #5a5658 55%, #2c2a2e);
  }
  .portrait--mic { left: 40px; top: 290px; width: 212px; height: 248px; transform: rotate(-3deg); }
  .portrait--temples { left: 46px; top: 548px; width: 212px; height: 240px; transform: rotate(3deg); }
  .portrait--stage { left: 40px; top: 795px; width: 212px; height: 260px; transform: rotate(-2deg);
    background: linear-gradient(180deg, #0f1630, #1f2f6a 60%, #0d1224); }

  .feature-panel {
    position: absolute; left: 340px; top: 340px; width: 520px; height: 450px;
    background: var(--panel); text-align: center; color: var(--white); padding: 34px 30px 0;
  }
  .feature-panel__quote {
    font-family: "Baloo 2", sans-serif; font-weight: 500; font-style: italic;
    font-size: 44px; line-height: 50px; text-shadow: 2px 3px 4px rgba(0,0,0,0.7);
  }
  .feature-panel__copy { margin-top: 20px; font-size: 23px; line-height: 30px; }
  .feature-panel__copy strong { font-family: "Archivo Black", sans-serif; font-weight: 400; color: var(--ink-blue); }
  .feature-panel__clients { margin-top: 26px; font-size: 23px; line-height: 30px; font-weight: 700; font-style: italic; }

  .corporate-note {
    position: absolute; left: 320px; top: 900px; width: 580px;
    font-size: 21px; line-height: 27px;
  }

  .assignments {
    position: absolute; left: 0; top: 1000px; width: 927px; height: 84px;
    background: var(--sky-pale); text-align: center; padding-top: 6px;
  }
  .assignments__title { font-size: 25px; font-weight: 700; color: var(--ink-blue); line-height: 30px; }
  .assignments__list { font-size: 20px; line-height: 24px; }

  .testimonial { position: absolute; top: 1088px; width: 330px; text-align: center; }
  .testimonial--left { left: 60px; }
  .testimonial--right { left: 560px; }
  .testimonial__star { position: absolute; left: 115px; top: -4px; width: 100px; height: 66px; z-index: 0; }
  .testimonial__quote {
    position: relative; z-index: 1; font-family: "Noto Serif", serif; font-style: italic; font-weight: 700;
    color: var(--ink-blue); font-size: 25px; line-height: 30px;
  }
  .testimonial__source { position: relative; z-index: 1; font-size: 15px; line-height: 18px; }

  .site-footer {
    position: absolute; left: 0; top: 1158px; width: 927px; height: 42px;
    background: var(--sky-pale); text-align: center;
    font-size: 17px; font-weight: 700; color: var(--ink-blue); line-height: 42px;
  }
</style>
</head>
<body>
<div class="flyer">
  <div class="starfield" role="img" aria-label="Deep night sky filled with stars"></div>

  <svg class="sky-curve" viewBox="0 0 927 420" aria-hidden="true">
    <path d="M0 0 H927 V400 C880 330 820 260 720 210 C560 150 300 150 0 170 Z" fill="var(--sky)"/>
  </svg>

  <h2 class="headline">Experience the sophisticated Comedy<br>and Mind-Reading of Mentalist</h2>
  <h1 class="performer-name">JULIAN MARSH</h1>

  <div class="portrait portrait--mic" role="img" aria-label="Portrait of the mentalist smiling, holding a microphone"></div>
  <div class="portrait portrait--temples" role="img" aria-label="Portrait of the mentalist with fingers at his temples"></div>
  <div class="portrait portrait--stage" role="img" aria-label="The mentalist performing on stage in a blue suit"></div>

  <section class="feature-panel">
    <p class="feature-panel__quote">"Australia's Magician<br>of the Mind"</p>
    <p class="feature-panel__copy"><strong>Booked and rebooked</strong> by the<br><em>world's leading Cruise Lines</em><br>to provide <strong>sophisticated<br>entertainment</strong> for their<br>discerning audiences.</p>
    <p class="feature-panel__clients">Coralline, Meridian, Silverwake,<br>Regalia, Southern Star Cruises.</p>
  </section>

  <p class="corporate-note">Corporate &amp; Association clients also take him around the world for his astounding, interactive and easily staged show or to provide his unique MC services.</p>

  <section class="assignments">
    <h3 class="assignments__title">Recent assignments</h3>
    <p class="assignments__list">Hawaii, New Zealand, South Africa,<br>Hong Kong and all states of Australia.</p>
  </section>

  <div class="testimonial testimonial--left">
    <svg class="testimonial__star" viewBox="0 0 100 66" aria-hidden="true">
      <polygon points="50,0 62,24 98,26 70,42 80,66 50,52 20,66 30,42 2,26 38,24" fill="var(--star)"/>
    </svg>
    <p class="testimonial__quote">"Outstanding!"</p>
    <p class="testimonial__source">CEO, Pacific Business Council</p>
  </div>
  <div class="testimonial testimonial--right">
    <svg class="testimonial__star" viewBox="0 0 100 66" aria-hidden="true">
      <polygon points="50,0 62,24 98,26 70,42 80,66 50,52 20,66 30,42 2,26 38,24" fill="var(--star)"/>
    </svg>
    <p class="testimonial__quote">"Brilliant!"</p>
    <p class="testimonial__source">CEO, Redgum Masonry</p>
  </div>

  <footer class="site-footer">www.MindReaderOz.com</footer>
</div>
</body>
</html>
```